Kelvard Engineers: Why you should hire us keepsake

New design. Open to plastic cards. We are an engineering firm that designs cell phone towers and commercial buildings. Please check out our website www.kelvardeng.example for more details. We want people to remember our card and for it to be useful if possible. We want the same look and feel on these cards to be translated to other marketing material we may need such as brochures.

Target Market(s)

Architects, Developers and Telecommunication Carriers

Industry/Entity Type

Engineering

Contact Information for Business Card

Card with our company colors, logo, and innovative design with elements related to our industry.

Font styles to use
Sans Serif

Colors
9bcb3c
abd036
0255a3

Requirements
Must have
• Sleek and hip design
Nice to have
• Bright lime green and navy coloring that pops with an innovative design.
Should not have
• A basic and boring design

```html
<!DOCTYPE html>
<html lang="en">
<head>
<meta charset="utf-8">
<title>Kelvard Engineers – Business Card</title>
<link rel="stylesheet" href="https://fonts.googleapis.com/css2?family=Source+Sans+3:wght@400;600;900&display=swap">
<style>
  :root {
    --backdrop: #666666;
    --card-white: #ffffff;
    --navy: #002c5c;
    --lime: #19f21a;
    --ink: #1d1d1d;
  }
  * { box-sizing: border-box; margin: 0; padding: 0; }
  html, body {
    width: 1200px; height: 900px; overflow: hidden;
    background: var(--backdrop);
    font-family: "Source Sans 3", "Myriad Pro", Arial, sans-serif;
  }
  .stage { position: relative; width: 1200px; height: 900px; }
  .card {
    position: absolute; top: 170px;
    width: 347px; height: 561px;
    overflow: hidden;
  }
  .card--front { left: 259px; background: var(--card-white); }
  .card--back { left: 631px; background: var(--navy); }

  .brand {
    position: absolute; left: 0; right: 0;
    text-align: center;
    font-size: 80px;
    font-weight: 900;
    color: var(--lime);
    letter-spacing: -1px;
    line-height: 1;
  }
  .card--front .brand { top: 136px; }
  .card--back .brand { top: 238px; }

  .signal {
    position: absolute;
    fill: none;
    stroke-linecap: round;
  }
  .card--front .signal { top: 22px; right: 22px; width: 64px; height: 64px; stroke: var(--navy); opacity: 0.18; }
  .card--back .signal { top: 24px; right: 24px; width: 80px; height: 80px; stroke: var(--lime); opacity: 0.35; }

  .edge-band {
    position: absolute; left: 0; right: 0; bottom: 0; height: 8px;
  }
  .card--front .edge-band { background: var(--navy); }
  .card--back .edge-band { background: var(--lime); }

  .holder-name {
    position: absolute; top: 356px; left: 0; right: 0;
    text-align: center;
    font-size: 20px; font-weight: 600;
    color: var(--lime);
    letter-spacing: 0.3px;
  }
  .contact {
    position: absolute; top: 409px; left: 0; right: 0;
    list-style: none;
    text-align: center;
    font-size: 15px; line-height: 20.5px;
    color: var(--ink);
  }
  .contact .label { color: var(--lime); font-weight: 600; }
  .contact .web { color: var(--lime); }
  .discipline {
    position: absolute; top: 508px; left: 0; right: 0;
    text-align: center;
    font-size: 15px;
    color: var(--navy);
    letter-spacing: 0.2px;
  }
</style>
</head>
<body>
  <main class="stage">
    <section class="card card--front" aria-label="Business card front">
      <svg class="signal" viewBox="0 0 64 64" aria-hidden="true">
        <path d="M52 40 A20 20 0 0 0 32 20" stroke-width="4"/>
        <path d="M62 40 A30 30 0 0 0 32 10" stroke-width="4"/>
        <circle cx="32" cy="40" r="5" fill="currentColor" stroke="none"/>
      </svg>
      <div class="brand">Kelvard</div>
      <h1 class="holder-name">DANA WHITLOW MARSH</h1>
      <ul class="contact">
        <li><span class="label">P:</span> 555.014.2870</li>
        <li><span class="label">M:</span> 555.019.4413</li>
        <li><span class="label">E:</span> DMARSH@kelvardeng.example</li>
        <li class="web">www.kelvardeng.example</li>
      </ul>
      <p class="discipline">MULTI-DISCIPLINE ENGINEERING</p>
      <div class="edge-band"></div>
    </section>
    <section class="card card--back" aria-label="Business card back">
      <svg class="signal" viewBox="0 0 64 64" aria-hidden="true">
        <path d="M52 40 A20 20 0 0 0 32 20" stroke-width="3"/>
        <path d="M62 40 A30 30 0 0 0 32 10" stroke-width="3"/>
      </svg>
      <div class="brand">Kelvard</div>
      <div class="edge-band"></div>
    </section>
  </main>
</body>
</html>
```